Neue Website fuer Software-Firma (CMS: Joomla, Responsive Design)
Zielgruppe
Die VANTRIX ist ein Software- und Beratungshaus im Lager- und Produktionslogistikbereich. Unsere Kunden sind Industriefirmen und Logistikdienstleister, die ein oder mehrere Laeger bewirtschaften und dafuer eine Software und mobile Datenerfassung einsetzen. Fast alle unserer Kunden haben KVT im Einsatz.
Aufgabenstellung
Unsere aktuelle Website wurde seit langem nicht mehr gepflegt und ist veraltet.
Wir moechten die neue Website gern mit dem CMS Joomla betreiben (ggf. waere auch Wordpress moeglich). Gern koennen Sie als Basis ein bereits existierendes (freies) Theme verwenden, wenn es entweder bereits alle Ansprueche erfuellt oder Sie es entsprechend anpassen.
Die neue Website soll in jedem Fall responsive sein, d.h. sowohl auf Desktop, Tablet und Smartphone funktionieren und das Design entsprechend anpassen.
Unsere aktuelle Seite steht unter www.vantrix-lagerwerk.example
Eine Seite, die uns besonders gut gefaellt, ist www.quendal.example (die sich auch teilweise an die gleichen Kunden richtet).
Wir moechten ein klares Design. Ein Beispiel, wie eines unserer Dashboards unserer Software aussieht, finden Sie anbei. Die Farbgestaltung darin wird jedoch noch geaendert. Sie wird eher in Richtung der Farbgestaltung der Quendal-Website gehen, jedoch immer noch grundsaetzlich hell sein. Evtl. koennen Sie Elemente daraus aufgreifen? Es soll in jedem Fall ersichtlich sein, dass Website und Software von der gleichen Firma sind.
Es soll moeglichst viel mit Grafiken gearbeitet werden – aehnlich der Quendal-Seite unter der Dia-Show. Diese muessen aber nicht zwingend farbig sein. Ein Mockup fuer einfarbige Grafiken unterhalb einer Diashow habe ich hier erstellt: https://helgard07.seitenbau.example/meinewebsite-1 Bitte orientieren Sie sich aber nicht an dieser Seite selbst – das war nur ein Probierbeispiel.
Desweiteren soll die Seite suchmaschinenfreundlich sein.
In Ihren Leistungen enthalten sein soll:
- Erstellung der Homepage incl.
o Menu (wie bei Quendal soll es ausklappbar sein und mind. 2 Ebenen koennen)
o Login-Button der einen externen Link aufruft
o Auswahl der Sprache (und damit Verlinkung zu jeweils der Homepage in der
ausgewaehlten Sprache
o Moeglichkeit zum Chat
o Suchfeld zum Durchsuchen aller S..

```html
<!DOCTYPE html>
<html lang="de">
<head>
<meta charset="utf-8">
<title>VANTRIX – Software Solutions for Logistics</title>
<link href="https://fonts.googleapis.com/css2?family=Mulish:wght@400;600;700;800&display=swap" rel="stylesheet">
<style>
:root{
  --bg-outer:#2b4468;
  --navy:#0d3a97;
  --blue:#1a45a3;
  --link:#2ea3f2;
  --text:#3a3a3a;
  --muted:#6a6a6a;
  --light:#f4f4f4;
  --red:#d9202a;
  --white:#ffffff;
}
*{box-sizing:border-box;margin:0;padding:0}
html,body{width:1200px;height:2596px;overflow:hidden}
body{background:var(--bg-outer);font-family:'Mulish',sans-serif;color:var(--text);position:relative}
.page{position:absolute;left:120px;top:0;width:960px;height:2596px}
section,header,footer{position:absolute;left:0;width:960px}
.abs{position:absolute}

/* header */
.site-header{top:0;height:110px;background:var(--white)}
.topbar{right:48px;top:5px;display:flex;gap:10px;align-items:center;font-size:8px;color:var(--navy);font-weight:600}
.topbar .soc{display:flex;gap:9px}
.topbar .soc span{width:7px;height:7px;border-radius:50%;background:var(--navy);display:block}
.brand{left:50px;top:40px}
.brand-name{font-size:30px;font-weight:700;color:var(--navy);line-height:32px}
.brand-tag{font-size:10px;font-weight:400;color:#444;margin-top:4px}
.nav{left:316px;top:68px;display:flex;gap:17px;font-size:9.5px;font-weight:600;color:var(--navy)}
.nav .active{color:var(--link)}
.lang{left:641px;top:60px;width:69px;height:29px;background:#eeeeee;border:1px solid #ddd;font-size:9px;color:#555;padding:9px 11px}
.lang b{position:absolute;right:0;top:0;width:10px;height:27px;background:#ccc}
.search{left:727px;top:60px;width:120px;height:29px;background:#eef0f3}
.search-btn{left:847px;top:60px;width:57px;height:29px;background:var(--navy);color:#fff;font-size:9px;font-weight:700;text-align:center;line-height:29px}

/* hero */
.hero{top:110px;height:328px;background:linear-gradient(100deg,#3f7d98 0%,#5aa6bd 55%,#4d8ea6 100%)}
.hero h1{left:65px;top:67px;width:460px;font-size:30px;line-height:41px;font-weight:700;color:var(--blue)}
.hero p{left:65px;top:156px;width:440px;font-size:11.5px;line-height:21px;color:#25536a}
.btn{background:var(--navy);color:#fff;font-weight:700;font-size:10.5px;display:flex;align-items:center;justify-content:center;gap:6px}
.btn svg{width:14px;height:14px}
.hero .btn{left:65px;top:219px;width:194px;height:43px}
.dots{left:462px;top:292px;display:flex;gap:6px}
.dots span{width:4px;height:4px;border-radius:50%;background:#d8e6ec;opacity:.6}
.dots span:first-child{opacity:1;background:#fff}
.hero-photo{left:570px;top:0;width:390px;height:328px;background:linear-gradient(180deg,#2c4f8c 0%,#6f8fb8 45%,#8aa4c0 100%)}

/* services */
.services{top:438px;height:319px;background:var(--light)}
.service{top:25px;width:172px}
.service .icon{width:90px;height:76px;border-radius:8px}
.service h3{margin-top:27px;font-size:15px;font-weight:700;color:var(--blue)}
.service p{margin-top:10px;font-size:10.8px;line-height:20.8px;color:#333}

/* cta */
.cta{top:757px;height:128px;background:linear-gradient(100deg,#4a8aa2 0%,#62b3c9 50%,#4c8ca4 100%)}
.cta h2{left:47px;top:54px;font-size:16.5px;font-weight:700;color:#fff}
.cta .btn{left:781px;top:42px;width:122px;height:43px}

/* titles */
.sec-title{left:287px;width:378px;height:38px;border:2px dotted #a9b8cc;text-align:center;line-height:34px;font-size:16.5px;font-weight:700;color:var(--blue)}

/* news */
.news{top:885px;height:581px;background:#f2f2f2}
.news .sec-title{top:63px}
.card{top:156px;width:256px;height:375px;background:#fff}
.card .img{width:256px;height:160px}
.card h4{margin:19px 13px 0;font-size:11.5px;font-weight:700;color:var(--blue)}
.card .date{margin:11px 13px 0;font-size:10.5px;color:var(--muted)}
.card p{margin:7px 13px 0;font-size:10.8px;line-height:20.8px;color:var(--muted)}

/* clients */
.clients{top:1476px;height:386px;background:#fff}
.clients .sec-title{top:62px}
.client{width:200px;text-align:center;font-size:20px;font-weight:700;color:var(--navy);display:flex;align-items:center;justify-content:center;gap:8px}

/* contact + footer */
.contact{top:1872px;height:724px;background:linear-gradient(180deg,#4b7487 0%,#3c5d74 45%,#2e4254 100%)}
.contact .sec-title{top:62px;color:#fff;border-color:#c9d6e0}
.field{background:#fff;border:1px solid #dfe4ea;font-size:10.5px;color:#555;padding:11px 11px}
.captcha{left:720px;top:335px;width:32px;height:34px;background:#fff}
.contact .btn{left:764px;top:332px;width:140px;height:43px}
.fcol{top:486px;width:190px;color:#fff;font-size:10.8px;line-height:20.8px}
.fcol h5{font-size:11.5px;font-weight:700;margin-bottom:4px}
.fcol li{list-style:none;padding-left:9px;position:relative;margin-bottom:5px}
.fcol li:before{content:"";position:absolute;left:0;top:8px;width:3px;height:3px;border-radius:50%;background:#fff}
.social{left:725px;top:511px;width:180px;display:grid;grid-template-columns:88px 88px;gap:4px}
.social div{height:52px;color:#fff;font-size:9px;font-weight:700;display:flex;flex-direction:column;align-items:center;justify-content:center;gap:6px}
.social i{width:18px;height:18px;border-radius:50%;background:rgba(255,255,255,.3);display:block}
.bottombar{left:0;top:688px;width:960px;height:36px;background:#2a3b4b;font-size:9px;color:#c9d3dc;display:flex;gap:17px;padding:14px 47px}
.chat{left:1148px;top:2524px;width:40px;height:40px;background:var(--red);display:flex;align-items:center;justify-content:center}
</style>
</head>
<body>
<div class="page">

<header class="site-header">
  <div class="abs topbar">
    <span>☎ +49 000 555 0140</span>
    <span>✉ info@vantrix-lagerwerk.example</span>
    <span class="soc"><span></span><span></span><span></span></span>
  </div>
  <div class="abs brand">
    <div class="brand-name">VANTRIX</div>
    <div class="brand-tag">Software Solutions For Logistics</div>
  </div>
  <nav class="abs nav">
    <span class="active">Home</span><span>News</span><span>Products ▾</span><span>Clients ▾</span><span>Company ▾</span><span>Contact</span>
  </nav>
  <div class="abs lang">English<b></b></div>
  <div class="abs search"></div>
  <div class="abs search-btn">Search</div>
</header>

<section class="hero">
  <h1 class="abs">Choose a background picture that suites your color scheme</h1>
  <p class="abs">Optional: Write some text but keep it short and simple. Use keywords for SEO. Talk to your target group. Encourage users to browse your website.</p>
  <div class="abs btn">Warehouse Management
    <svg viewBox="0 0 16 16"><circle cx="8" cy="8" r="7" fill="none" stroke="#fff" stroke-width="1.4"/><path d="M7 5l3 3-3 3" fill="none" stroke="#fff" stroke-width="1.4"/></svg></div>
  <div class="abs dots"><span></span><span></span><span></span></div>
  <div class="abs hero-photo" role="img" aria-label="Photo of a truck parked inside a large warehouse hall"></div>
</section>

<section class="services">
  <div class="abs service" style="left:47px"><div class="icon" role="img" aria-label="Production icon illustration" style="background:linear-gradient(135deg,#1a45a3,#4f74c8)"></div><h3>Production</h3><p>At vero eos et accusam et justo duo dolores et ea rebum. Stet clita kasd gubergren, no sea takimata sanctus est Lorem ipsum dolor sit amet.</p></div>
  <div class="abs service" style="left:274px"><div class="icon" role="img" aria-label="Warehousing icon illustration" style="background:linear-gradient(135deg,#e2334a,#5a6f85)"></div><h3>Warehousing</h3><p>At vero eos et accusam et justo duo dolores et ea rebum. Stet clita kasd gubergren, no sea takimata sanctus est Lorem ipsum dolor sit amet.</p></div>
  <div class="abs service" style="left:501px"><div class="icon" role="img" aria-label="KVT icon illustration with charts" style="background:linear-gradient(135deg,#3bb26b,#e2334a)"></div><h3>KVT</h3><p>At vero eos et accusam et justo duo dolores et ea rebum. Stet clita kasd gubergren, no sea takimata sanctus est Lorem ipsum dolor sit amet.</p></div>
  <div class="abs service" style="left:728px"><div class="icon" role="img" aria-label="Automation icon illustration with conveyor" style="background:linear-gradient(135deg,#e2334a,#7c8a96)"></div><h3>Automation</h3><p>At vero eos et accusam et justo duo dolores et ea rebum. Stet clita kasd gubergren, no sea takimata sanctus est Lorem ipsum dolor sit amet.</p></div>
</section>

<section class="cta">
  <h2 class="abs">Our Management is commited to solve your internal logistics problems.</h2>
  <div class="abs btn">Learn more
    <svg viewBox="0 0 16 16"><circle cx="8" cy="8" r="7" fill="none" stroke="#fff" stroke-width="1.4"/><path d="M7 5l3 3-3 3" fill="none" stroke="#fff" stroke-width="1.4"/></svg></div>
</section>

<section class="news">
  <div class="abs sec-title">Latest news</div>
  <article class="abs card" style="left:47px"><div class="img" role="img" aria-label="Photo of a passenger airplane at an airport" style="background:linear-gradient(180deg,#6d7b8e,#9aa3ad)"></div><h4>Example for a news article 3</h4><div class="date">Sep 25, 2017</div><p>Lorem ipsum dolor sit amet, consectetuer adipiscing elit. Aenean commodo ligula eget dolor. Aenean massa. Cum sociis natoque penatibus et magnis dis parturient montes, nascetur ridiculus mus. Donec quam felis, ultricies nec, pellentesque eu, pretium quis, sem. Nulla...</p></article>
  <article class="abs card" style="left:351px"><div class="img" role="img" aria-label="Photo of an office desk with computer screens" style="background:linear-gradient(180deg,#c9ccd2,#5b6170)"></div><h4>Example for a news article 2</h4><div class="date">Sep 25, 2017</div><p>Lorem ipsum dolor sit amet, consectetuer adipiscing elit. Aenean commodo ligula eget dolor. Aenean massa. Cum sociis natoque penatibus et magnis dis parturient montes, nascetur ridiculus mus. Donec quam felis, ultricies nec, pellentesque eu, pretium quis, sem. Nulla...</p></article>
  <article class="abs card" style="left:655px"><div class="img" role="img" aria-label="Photo of an empty warehouse hall" style="background:linear-gradient(180deg,#2c4f8c,#7f9cc0)"></div><h4>Example for a news article</h4><div class="date">Sep 25, 2017</div><p>Lorem ipsum dolor sit amet, consectetuer adipiscing elit. Aenean commodo ligula eget dolor. Aenean massa. Cum sociis natoque penatibus et magnis dis parturient montes, nascetur ridiculus mus. Donec quam felis, ultricies nec, pellentesque eu, pretium quis, sem. Nulla...</p></article>
</section>

<section class="clients">
  <div class="abs sec-title">Our clients</div>
  <div class="abs client" style="left:19px;top:152px;height:76px">Norvalen</div>
  <div class="abs client" style="left:259px;top:152px;height:76px">Kestra</div>
  <div class="abs client" style="left:499px;top:152px;height:76px">Brannow</div>
  <div class="abs client" style="left:739px;top:152px;height:76px">Miravel</div>
  <div class="abs client" style="left:19px;top:252px;height:70px">Tellig</div>
  <div class="abs client" style="left:259px;top:252px;height:70px">Sunmark</div>
  <div class="abs client" style="left:499px;top:252px;height:70px">Haus Weilbach AG</div>
  <div class="abs client" style="left:739px;top:252px;height:70px">Orvion</div>
</section>

<footer class="contact">
  <div class="abs sec-title">Drop us a line</div>
  <div class="abs field" style="left:47px;top:156px;width:416px;height:34px">Name</div>
  <div class="abs field" style="left:489px;top:156px;width:416px;height:34px">E-Mail-Adresse</div>
  <div class="abs field" style="left:47px;top:216px;width:858px;height:96px">Nachricht</div>
  <div class="abs captcha"></div>
  <div class="abs btn">Send message
    <svg viewBox="0 0 16 16"><circle cx="8" cy="8" r="7" fill="none" stroke="#fff" stroke-width="1.4"/><path d="M7 5l3 3-3 3" fill="none" stroke="#fff" stroke-width="1.4"/></svg></div>

  <div class="abs fcol" style="left:47px"><h5>About VANTRIX.</h5>Put anything in the footer. For example a short text about your company. Stet clita kasd gubergren, no sea takimata sanctus est Lorem ipsum dolor sit amet.</div>
  <div class="abs fcol" style="left:274px"><h5>Recent Posts</h5><ul><li>Example for a news article 3</li><li>Example for a news article 2</li><li>Example for a news article</li></ul></div>
  <div class="abs fcol" style="left:501px"><h5>Quick links</h5><ul><li>Menu item in footer area</li><li>Menu item in footer area</li><li>Menu item in footer area</li><li>Menu item in footer area</li></ul></div>
  <div class="abs fcol" style="left:728px"><h5>Follow Us</h5></div>
  <div class="abs social">
    <div style="background:#3d5a96"><i></i>Friendly</div>
    <div style="background:#1eaae6"><i></i>Chirper</div>
    <div style="background:#d9483a"><i></i>Circles</div>
    <div style="background:#1b86bd"><i></i>Linkwork</div>
  </div>
  <div class="abs bottombar"><span>Company details</span><span>Terms of Use and Privacy</span><span>Login</span></div>
</footer>

</div>
<div class="abs chat"><svg width="16" height="16" viewBox="0 0 16 16"><path d="M2 3h12v8H7l-3 3v-3H2z" fill="#fff"/></svg></div>
</body>
</html>
```